Velmora Diagnostics Website

Project Description – Velmora Website Design
We need a clean, modern, and professional website for Velmora Diagnostics, a Ashgrove Hollis University of Dunmere spin-out focused on early cancer detection. Our first product, GlandSURE™, is a urine-based risk assessment test for pancreatic cancer, supported by strong clinical validation and partnerships with leading hospitals.

The site should:

Communicate trust, innovation, and clinical credibility.
Feature a clear value proposition on the home page with strong calls to action for investors, clinicians, and partners.
Showcase our technology, science, and clinical evidence in a way that is accessible but authoritative.
Highlight our university heritage, team, and collaborators.
Include sections for products/services, news/press, and contact forms.
Be fully responsive, WordPress compatible, SEO-friendly, and WCAG 2.1 AA accessible.

We want a minimalist, elegant design with subtle animations, strong visuals (e.g., science/biotech imagery), and a clear structure for future growth.
Deliverables should include editable design files (Figma/Sketch/Adobe XD) and a style guide.

```html
<!DOCTYPE html>
<html lang="en">
<head>
<meta charset="utf-8">
<title>Velmora DX – Early Cancer Detection</title>
<link rel="stylesheet" href="https://fonts.googleapis.com/css2?family=Poppins:wght@400;500;600;700&display=swap">
<style>
:root{
  --navy:#1c1a70;
  --navy-deep:#14105a;
  --blue:#3a88d8;
  --blue-light:#5cc2ee;
  --yellow:#f6c431;
  --card:#e5f4fb;
  --grey:#f3f3f3;
  --text:#333344;
  --white:#ffffff;
}
*{box-sizing:border-box;margin:0;padding:0}
html,body{width:1200px;height:3726px;overflow:hidden}
body{font-family:'Poppins',sans-serif;color:var(--text);background:var(--white);position:relative}
section,header,footer{position:absolute;left:0;width:1200px}
.abs{position:absolute}
.brand{display:flex;align-items:center;gap:12px;color:var(--blue);font-weight:500;letter-spacing:1px}
.brand-dot{border-radius:50%;background:var(--blue)}
.btn{position:absolute;display:flex;align-items:center;justify-content:center;border-radius:30px;font-weight:600;color:var(--white);background:var(--yellow);font-size:15px}

/* header */
.site-header{top:0;height:82px;background:var(--white)}
.site-header .brand{position:absolute;left:75px;top:20px;font-size:22px}
.nav{position:absolute;top:33px;font-size:15px;font-weight:600;color:var(--navy)}
.nav.active{color:var(--blue)}

/* hero */
.hero{top:82px;height:728px;background:radial-gradient(circle at 20% 30%,#1e3f9a,#142a78 45%,#0f1f5c 100%);overflow:hidden}
.hero-photo{left:600px;top:0;width:600px;height:728px;background:linear-gradient(100deg,rgba(20,42,120,0) 0%,#6f9fd6 30%,#c9def0 65%,#eef4fa 100%)}
.hero h1{position:absolute;left:75px;top:96px;font-size:43px;line-height:43px;color:var(--white);font-weight:700;letter-spacing:0.5px}
.hero .lead{position:absolute;left:75px;top:200px;font-size:22px;color:var(--white)}
.hero .lead mark{background:var(--yellow);color:var(--navy);font-weight:600;padding:2px 8px}
.feature{position:absolute;left:75px;display:flex;align-items:center;gap:14px;color:var(--white);font-weight:600;font-size:16px}
.feature svg{width:34px;height:34px}
.hero .btn{left:75px;top:489px;width:268px;height:54px;background:var(--blue-light);font-size:19px}
.hero-curve{left:0;top:618px}
.badge{position:absolute;border-radius:50%;background:var(--white);box-shadow:0 4px 14px rgba(0,0,0,.15);display:flex;align-items:center;justify-content:center}
.badge span{width:40%;height:40%;border-radius:50%;background:var(--yellow)}

/* stats */
.stats{top:810px;height:211px}
.stat{position:absolute;width:320px;text-align:center}
.stat b{display:block;font-size:60px;line-height:70px;color:var(--yellow);font-weight:700}
.stat span{font-size:26px;color:#222;font-weight:500}

/* about */
.about{top:1021px;height:568px;background:var(--grey)}
.about-photo{left:0;top:65px;width:586px;height:437px;background:linear-gradient(120deg,#0b3b5e,#1f7fb0 40%,#7fb8d6 75%,#cfe2ee);border-radius:0 120px 0 0;clip-path:polygon(0 0,100% 0,74% 100%,0 100%)}
h2{font-size:38px;font-weight:700;color:var(--navy)}
.about h2{position:absolute;left:616px;top:55px}
.about p.body{position:absolute;left:616px;top:114px;width:512px;font-size:13.2px;line-height:24px}
.about .btn{left:616px;top:275px;width:150px;height:46px;font-size:14px}
.mv{position:absolute;top:347px;width:362px;height:133px;background:var(--white);border-left:5px solid var(--blue);padding:14px 18px;box-shadow:0 4px 12px rgba(0,0,0,.08)}
.mv h3{font-size:20px;color:var(--blue);font-weight:600;margin-bottom:4px}
.mv.vision h3{color:var(--navy)}
.mv p{font-size:13px;line-height:24px}

/* products */
.products{top:1589px;height:558px}
.products h2{position:absolute;left:74px;top:56px}
.arrow{position:absolute;top:72px;width:24px;height:24px}
.pcard{position:absolute;top:142px;width:328px;height:332px;border-radius:44px;background:var(--card);padding:24px 22px}
.pcard.featured{background:linear-gradient(135deg,#3a7fd5,#5cc2ee);color:var(--white)}
.pcard svg{width:66px;height:66px}
.pcard h3{font-size:19px;font-weight:600;color:var(--blue);margin:18px 0 8px}
.pcard.featured h3{color:var(--white)}
.pcard p{font-size:13.4px;line-height:24px}
.pcard .btn{left:22px;top:253px;width:150px;height:46px;font-size:14px}

/* news */
.news{top:2147px;height:529px;background:var(--grey)}
.news h2{position:absolute;width:1200px;text-align:center;top:64px}
.nimg{position:absolute;border-radius:6px}
.ntitle{position:absolute;font-size:17.5px;line-height:24px;color:var(--blue);font-weight:600}
.ndate{position:absolute;font-size:15px;color:var(--navy);font-weight:500}

/* contact */
.contact{top:2676px;height:577px}
.contact h2.center{position:absolute;width:1200px;text-align:center;top:64px}
.contact h3.side{position:absolute;left:75px;top:140px;font-size:27px;color:var(--blue);font-weight:600}
.contact .brand{position:absolute;left:75px;top:208px;font-size:26px}
.cinfo{position:absolute;left:75px;display:flex;gap:14px;align-items:flex-start}
.cinfo .ico{width:50px;height:50px;border-radius:50%;border:2px solid #e3e3ea;display:flex;align-items:center;justify-content:center}
.cinfo .ico svg{width:18px;height:18px}
.cinfo b{display:block;font-size:17px;color:var(--navy);font-weight:500}
.cinfo small{font-size:13px;line-height:22px;color:#333}
.form{position:absolute;left:434px;top:148px;width:692px;height:402px;border-radius:18px;background:var(--blue);padding:0}
.form h3{position:absolute;left:33px;top:20px;font-size:27px;color:var(--white);font-weight:600}
.field{position:absolute;background:var(--white);border-radius:22px;font-size:13px;color:#222;padding:13px 18px;font-weight:500}
.form .btn{left:33px;top:317px;width:295px;height:44px;font-size:15px}

/* footer */
.footer{top:3253px;height:473px;background:var(--navy)}
.footer .brand{position:absolute;left:75px;top:176px;font-size:25px;color:#5aa7e8}
.footer .about-text{position:absolute;left:75px;top:252px;width:340px;font-size:13px;line-height:26px;color:var(--white)}
.fcol{position:absolute;top:168px;color:var(--white)}
.fcol h4{font-size:17px;font-weight:600;margin-bottom:8px}
.fcol a{display:block;font-size:13px;line-height:33px;color:var(--white);text-decoration:none}
.trial{position:absolute;left:883px;top:313px;color:var(--white);font-size:17px;font-weight:600}
.trial em{display:block;font-style:normal;color:var(--yellow);font-size:15px}
.divider{position:absolute;left:0;top:405px;width:1200px;height:1px;background:rgba(255,255,255,.15)}
.copy{position:absolute;top:427px;width:1200px;text-align:center;font-size:12px;color:var(--white)}
</style>
</head>
<body>

<header class="site-header">
  <div class="brand"><span class="brand-dot" style="width:26px;height:26px"></span>Velmora DX</div>
  <nav>
    <span class="nav active" style="left:601px">Home</span>
    <span class="nav" style="left:681px">About Us</span>
    <span class="nav" style="left:784px">Products / Services</span>
    <span class="nav" style="left:967px">News</span>
    <span class="nav" style="left:1042px">Contact Us</span>
  </nav>
</header>

<section class="hero">
  <div class="abs hero-photo" role="img" aria-label="Scientist in protective cap and mask examining a sample under a laboratory microscope"></div>
  <h1>Lighting the Way to Early<br>Cancer Detection</h1>
  <p class="lead"><mark>Non-Invasive,</mark> Urine-based diagnostics.</p>
  <div class="feature" style="top:264px"><svg viewBox="0 0 34 34" fill="none" stroke="#f6c431" stroke-width="2"><circle cx="17" cy="17" r="14"/><path d="M11 11l12 12M23 11L11 23"/></svg>Non-invasive, painless</div>
  <div class="feature" style="top:318px"><svg viewBox="0 0 34 34" fill="none" stroke="#f6c431" stroke-width="2"><circle cx="14" cy="14" r="9"/><path d="M21 21l9 9"/></svg>Precision biomarkers</div>
  <div class="feature" style="top:372px"><svg viewBox="0 0 34 34" fill="none" stroke="#f6c431" stroke-width="2"><rect x="8" y="8" width="18" height="18"/><rect x="13" y="13" width="8" height="8"/><path d="M12 3v5M17 3v5M22 3v5M12 26v5M17 26v5M22 26v5M3 12h5M3 17h5M3 22h5M26 12h5M26 17h5M26 22h5"/></svg>AI-powered insights</div>
  <div class="feature" style="top:426px"><svg viewBox="0 0 34 34" fill="none" stroke="#f6c431" stroke-width="2"><circle cx="17" cy="17" r="13"/><path d="M11 17l4 4 8-8"/></svg>Clinically validated &amp; university spin-out heritage</div>
  <div class="btn">Request a Demo&nbsp;<svg width="18" height="18" viewBox="0 0 18 18"><circle cx="9" cy="9" r="8" fill="#fff"/><path d="M5 9h7M9 6l3 3-3 3" stroke="#5cc2ee" stroke-width="2" fill="none"/></svg></div>
  <svg class="abs hero-curve" width="1200" height="110" viewBox="0 0 1200 110">
    <path d="M450,30 Q900,10 1200,50 L1200,110 L450,110Z" fill="#1c1a70"/>
    <path d="M0,92 Q300,25 620,22 Q950,22 1200,80 L1200,110 L0,110Z" fill="#fff"/>
  </svg>
  <div class="badge" style="left:292px;top:603px;width:76px;height:76px"><span></span></div>
</section>

<section class="stats">
  <div class="stat" style="left:79px;top:20px"><b>86%</b><span>Sensitivity</span></div>
  <div class="stat" style="left:440px;top:20px"><b>90%</b><span>Specificity</span></div>
  <div class="stat" style="left:802px;top:20px"><b>&gt;1,000</b><span>Samples Validated</span></div>
</section>

<section class="about">
  <div class="abs about-photo" role="img" aria-label="Clinician touching a holographic data display in a modern lab"></div>
  <h2>About Us</h2>
  <p class="body">Nemo enim ipsam voluptatem quia voluptas sit aspernatur aut odit aut fugit, sed quia consequuntur magni dolores eos qui ratione voluptatem sequi nesciunt. Neque porro quisquam est, qui dolorem ipsum quia dolor sit amet, consectetur, adipisci velit, sed quia non numquam eius modi tempora incidunt ut labore et dolore magnam aliquam quaerat voluptatem sed do eiusmod tempor incididunt ut labore.</p>
  <div class="btn">Learn More</div>
  <div class="mv" style="left:374px"><h3>Mission</h3><p>“ Nemo enim ipsam voluptatem quia volup tas sit aspernatur aut odit aut fugit, sed quia consequuntur magni dolores.”</p></div>
  <div class="mv vision" style="left:763px"><h3>Vision</h3><p>“ Nemo enim ipsam voluptatem quia volup tas sit aspernatur aut odit aut fugit, sed quia consequuntur magni dolores.”</p></div>
</section>

<section class="products">
  <h2>Products / Services</h2>
  <svg class="arrow" style="left:1074px" viewBox="0 0 24 24" fill="none" stroke="#1c1a70" stroke-width="2.5"><path d="M15 4l-8 8 8 8"/></svg>
  <svg class="arrow" style="left:1106px" viewBox="0 0 24 24" fill="none" stroke="#3a88d8" stroke-width="2.5"><path d="M9 4l8 8-8 8"/></svg>
  <div class="pcard" style="left:75px">
    <svg viewBox="0 0 66 66" fill="none" stroke="#1c1a70" stroke-width="2"><rect x="24" y="14" width="32" height="44" rx="3"/><path d="M31 24h18M31 32h18M31 40h18M31 48h12"/><circle cx="14" cy="14" r="6"/><path d="M6 34c0-6 4-10 8-10s8 4 8 10"/></svg>
    <h3>GlandSURE™</h3>
    <p>Nemo enim ipsam voluptatem quia voluptas sit aspernatur aut odit aut fugit, sed quia consequuntur magni dolores eos qui ratione voluptatem.</p>
    <div class="btn">Learn More</div>
  </div>
  <div class="pcard featured" style="left:437px">
    <svg viewBox="0 0 66 66" fill="none" stroke="#f6c431" stroke-width="2"><rect x="18" y="18" width="30" height="30" rx="3"/><path d="M33 25v16M25 33h16M24 6v12M33 6v12M42 6v12M24 48v12M33 48v12M42 48v12M6 24h12M6 33h12M6 42h12M48 24h12M48 33h12M48 42h12"/></svg>
    <h3>Technology</h3>
    <p>Nemo enim ipsam voluptatem quia voluptas sit aspernatur aut odit aut fugit, sed quia consequuntur magni dolores eos qui ratione voluptatem.</p>
    <div class="btn">Learn More</div>
  </div>
  <div class="pcard" style="left:798px">
    <svg viewBox="0 0 66 66" fill="none" stroke="#1c1a70" stroke-width="2"><path d="M10 58h46M18 58v-8h30v8M34 50c10 0 14-8 12-16M30 12l10 4-8 18-10-4z"/><circle cx="20" cy="40" r="5"/></svg>
    <h3>Science / Clinical Evidence</h3>
    <p>Nemo enim ipsam voluptatem quia voluptas sit aspernatur aut odit aut fugit, sed quia consequuntur magni dolores eos qui ratione voluptatem.</p>
    <div class="btn">Learn More</div>
  </div>
</section>

<section class="news">
  <h2>News &amp; Updates</h2>
  <div class="nimg" style="left:75px;top:145px;width:292px;height:202px;background:linear-gradient(135deg,#1b4f7e,#5d9cc7)" role="img" aria-label="Clinician wearing a headset viewing medical scan data on a tablet"></div>
  <p class="ntitle" style="left:75px;top:363px;width:300px">Duis aute irure dolor in reprehenderit&nbsp; eiusmod tempor</p>
  <p class="ndate" style="left:75px;top:421px">Sep 18, 2025</p>
  <div class="nimg" style="left:395px;top:145px;width:292px;height:202px;background:linear-gradient(135deg,#e4e8ec,#b9c6d2)" role="img" aria-label="Doctor holding an anatomical model in a clinic"></div>
  <p class="ntitle" style="left:395px;top:363px;width:300px">Duis aute irure dolor in reprehenderit&nbsp; eiusmod tempor</p>
  <p class="ndate" style="left:395px;top:421px">Sep 18, 2025</p>
  <div class="nimg" style="left:704px;top:145px;width:179px;height:146px;background:linear-gradient(135deg,#12314f,#4a82ab)" role="img" aria-label="Hands using a smartphone with medical icons overlay"></div>
  <p class="ntitle" style="left:899px;top:157px;width:230px">Duis aute irure dolor in reprehenderit&nbsp; eiusmod tempor incididunt</p>
  <p class="ndate" style="left:899px;top:240px">Sep 18, 2025</p>
  <div class="nimg" style="left:704px;top:311px;width:179px;height:146px;background:linear-gradient(135deg,#c9d3db,#6f8696)" role="img" aria-label="Two researchers reviewing results on a tablet in a laboratory"></div>
  <p class="ntitle" style="left:899px;top:323px;width:230px">Duis aute irure dolor in reprehenderit&nbsp; eiusmod tempor incididunt</p>
  <p class="ndate" style="left:899px;top:406px">Sep 18, 2025</p>
</section>

<section class="contact">
  <h2 class="center">Contact Info</h2>
  <h3 class="side">Contact Info</h3>
  <div class="brand"><span class="brand-dot" style="width:40px;height:40px"></span>Velmora DX</div>
  <div class="cinfo" style="top:296px"><div class="ico"><svg viewBox="0 0 18 18" fill="#3a88d8"><path d="M1 4l5-2 6 2 5-2v12l-5 2-6-2-5 2z"/></svg></div><div><b>Address</b><small>48 Larkspur Row Suite 12,<br>Dunmere 40217, United State</small></div></div>
  <div class="cinfo" style="top:376px"><div class="ico"><svg viewBox="0 0 18 18" fill="#3a88d8"><path d="M4 1l3 4-2 2c1 2 3 4 5 5l2-2 4 3-2 3C8 16 2 10 1 4z"/></svg></div><div><b>Phone</b><small style="font-size:16px">+100-555-0142</small></div></div>
  <div class="cinfo" style="top:438px"><div class="ico"><svg viewBox="0 0 18 18" fill="#3a88d8"><rect x="1" y="3" width="16" height="12" rx="1"/><path d="M1 4l8 6 8-6" stroke="#fff" fill="none"/></svg></div><div><b>Email</b><small>hello@velmoradx.example</small></div></div>
  <div class="cinfo" style="top:500px;align-items:center"><div class="ico"><svg viewBox="0 0 18 18" fill="#3a88d8"><rect x="1" y="1" width="16" height="16" rx="2"/></svg></div><div><b>Connect to ProLink</b></div></div>
  <div class="form">
    <h3>Onboard your clinic</h3>
    <div class="field" style="left:33px;top:76px;width:295px;height:44px">Name</div>
    <div class="field" style="left:341px;top:76px;width:293px;height:44px">Email Address</div>
    <div class="field" style="left:33px;top:137px;width:295px;height:44px">Phone No</div>
    <div class="field" style="left:341px;top:137px;width:293px;height:44px">Subject</div>
    <div class="field" style="left:33px;top:196px;width:601px;height:106px;border-radius:16px">Message</div>
    <div class="btn">Submit Now</div>
  </div>
</section>

<footer class="footer">
  <svg class="abs" style="left:0;top:0" width="1200" height="110" viewBox="0 0 1200 110">
    <path d="M0,0 H1200 V58 Q700,98 0,0Z" fill="#fff"/>
    <path d="M0,0 Q700,98 1200,58 V72 Q700,112 0,34Z" fill="#f6c431"/>
  </svg>
  <div class="badge" style="left:834px;top:49px;width:76px;height:76px"><span></span></div>
  <div class="brand"><span class="brand-dot" style="width:40px;height:40px;background:#5aa7e8"></span>Velmora DX</div>
  <p class="about-text">“ Excepteur sint occaecat cupidatat non proident, sunt in culpa qui officia deserunt mollit anim id est laborum.”</p>
  <div class="fcol" style="left:481px"><h4>Quick Links</h4><a>Home</a><a>About</a><a>Science</a><a>Contact</a></div>
  <div class="fcol" style="left:695px"><h4>Legal</h4><a>Privacy Policy</a><a>Terms of Use</a><a>GDPR</a><a>Accessibility</a></div>
  <div class="fcol" style="left:883px"><h4>Compliance Markers</h4></div>
  <div class="abs" style="left:887px;top:214px;width:102px;height:74px;border-radius:50%;background:#2b7ac4"></div>
  <div class="abs" style="left:1020px;top:212px;width:64px;height:76px;border-radius:10px;background:#3a5ba8"></div>
  <p class="trial">Trial Registry ID<em>#2567400</em></p>
  <div class="divider"></div>
  <p class="copy">Copyright 2024 Velmora Diagnostics All Rights Reserved</p>
</footer>

</body>
</html>
```